Business / Discount Card

Looking to create a 2 sided business card. Front side to say "Thanks for flying with Tallwind Skyrides" then have link to "In-Flight Photos, www.tallwindskyrides.com.au, password: tallwind" Back side of card to have company logo, phone number, facebook & instagram logo and #tallwindskyrides. Also included on this side will be discount text "Book again and save 10%. Use discount code: tallwind10"Round Corner Card Templates are attached. Please ensure dimensions are correct.Thanks,

Font styles to use
Sans Serif

Colors
33a6d7
ffffff
000000

Requirements
Must have
• Logo
• Blue, White and Black color scheme

```html
<!DOCTYPE html>
<html lang="en">
<head>
<meta charset="UTF-8">
<title>Tallwind Skyrides – Business Card</title>
<link href="https://fonts.googleapis.com/css2?family=Josefin+Sans:wght@400;600;700&display=swap" rel="stylesheet">
<style>
  :root {
    --sky-blue: #33a6d7;
    --band-blue: #2b9bd4;
    --ink: #0b0b0c;
    --paper: #f1f1f1;
    --white: #ffffff;
    --stage: #d9dadc;
  }
  * { margin: 0; padding: 0; box-sizing: border-box; }
  html, body { width: 1200px; height: 1021px; overflow: hidden; }
  body {
    background: var(--stage);
    font-family: "Josefin Sans", sans-serif;
    position: relative;
  }
  .card {
    position: absolute;
    left: 250px;
    width: 700px;
    height: 400px;
    border-radius: 30px;
    overflow: hidden;
    box-shadow: 0 10px 26px rgba(0,0,0,0.22);
  }

  /* Thank-you side */
  .card--thanks { top: 55px; background: var(--ink); color: var(--white); text-align: center; }
  .thanks-mark {
    width: 86px; height: 86px; border-radius: 50%;
    background: var(--sky-blue);
    margin: 70px auto 22px;
  }
  .thanks-title { color: var(--sky-blue); font-weight: 600; font-size: 29px; letter-spacing: 0.5px; }
  .photo-info { margin-top: 34px; font-size: 22px; line-height: 30px; letter-spacing: 0.6px; }
  .photo-info .url { font-weight: 700; }
  .photo-info .url span { color: var(--sky-blue); }

  /* Offer side */
  .card--offer { top: 535px; background: linear-gradient(160deg, #f7f7f7, #e4e4e4); }
  .offer-band { position: absolute; inset: 0; width: 100%; height: 100%; }
  .brand {
    position: absolute; top: 50px; left: 0; right: 0;
    display: flex; align-items: center; justify-content: center; gap: 18px;
  }
  .brand-dot { width: 54px; height: 54px; border-radius: 50%; background: var(--ink); }
  .brand-name { color: var(--sky-blue); font-weight: 700; font-size: 60px; letter-spacing: 1px; }
  .offer-line {
    position: absolute; top: 168px; left: 0; right: 0; text-align: center;
    font-size: 21px; color: var(--ink); letter-spacing: 0.3px;
  }
  .offer-line strong { color: var(--sky-blue); font-weight: 700; }
  .contacts {
    position: absolute; left: 20px; right: 20px; top: 306px; height: 72px;
    display: flex; align-items: center; color: var(--white);
  }
  .contact {
    flex: 1; height: 100%; display: flex; flex-direction: column; align-items: center; justify-content: center; gap: 8px;
    font-size: 20px; letter-spacing: 0.4px; white-space: nowrap;
  }
  .contact + .contact { border-left: 2px solid var(--white); }
  .contact-icon { width: 22px; height: 22px; }
  .icon-circle { border: 2.5px solid var(--white); border-radius: 50%; }
  .icon-square { background: var(--white); border-radius: 4px; }
</style>
</head>
<body>

  <section class="card card--thanks">
    <div class="thanks-mark"></div>
    <h1 class="thanks-title">Thanks for flying with Tallwind Skyrides</h1>
    <div class="photo-info">
      <p>In-Flight Photos</p>
      <p class="url">www.<span>tallwindskyrides</span>.com.au</p>
      <p>password: tallwind</p>
    </div>
  </section>

  <section class="card card--offer">
    <svg class="offer-band" viewBox="0 0 700 400" preserveAspectRatio="none" aria-hidden="true">
      <path d="M0 250 C 200 236, 480 258, 700 292 L700 400 L0 400 Z" fill="#0b0b0c"/>
      <path d="M0 256 C 200 242, 480 265, 700 299 L700 400 L0 400 Z" fill="#2b9bd4"/>
    </svg>
    <div class="brand">
      <div class="brand-dot"></div>
      <div class="brand-name">Tallwind Skyrides</div>
    </div>
    <p class="offer-line">Book again and <strong>SAVE 10%</strong> - Use discount code: <strong>tallwind10</strong></p>
    <div class="contacts">
      <div class="contact">
        <svg class="contact-icon" viewBox="0 0 24 24" aria-hidden="true">
          <path fill="#ffffff" d="M6.6 10.8a15 15 0 0 0 6.6 6.6l2.2-2.2a1 1 0 0 1 1-.25 11.4 11.4 0 0 0 3.6.57 1 1 0 0 1 1 1V20a1 1 0 0 1-1 1A17 17 0 0 1 3 4a1 1 0 0 1 1-1h3.5a1 1 0 0 1 1 1c0 1.25.2 2.450.57 3.57a1 1 0 0 1-.25 1z"/>
        </svg>
        <span>(555) 014-2290</span>
      </div>
      <div class="contact">
        <div class="contact-icon icon-circle"></div>
        <span>#tallwindskyrides</span>
      </div>
      <div class="contact">
        <div class="contact-icon icon-square"></div>
        <span>/tallwindskyrides</span>
      </div>
    </div>
  </section>

</body>
</html>
```